All-Natural Head Lice Removal company

I need a business card with my pre-existing logo. We are a new company located in Portland Oregon that goes into peoples homes to help with head lice removal. My products and approach are all- natural and also will be around children.On my current logo we used Teal Bl and the color Green. I am open to new ideas just want it simple and creative

Target Market(s)

my biggest market is families of school aged children

Industry/Entity Type

Business

Contact Information for Business Card

see upload for details from previous business card

Font styles to use
Serif

Colors
33a6d7
9bcb3b
f37122

Requirements
Must have
• Basic information/ logo put into a creative format that is catching to the eye
Nice to have
• creative

```html
<!DOCTYPE html>
<html lang="en">
<head>
<meta charset="utf-8">
<title>Nit Clear – Business Card</title>
<link rel="stylesheet" href="https://fonts.googleapis.com/css2?family=Lato:wght@300;400;700;900&display=swap">
<style>
  :root {
    --bg: #e9e7e3;
    --white: #fbfbfa;
    --band: #6b6c6c;
    --green: #7cc242;
    --green-dark: #5e9a2c;
    --ink: #4a4a4a;
    --ink-soft: #777777;
    --light: #ffffff;
  }
  * { margin: 0; padding: 0; box-sizing: border-box; }
  html, body {
    width: 1200px; height: 799px; overflow: hidden;
    background: var(--bg);
    font-family: "Lato", Arial, sans-serif;
  }
  .stage { position: relative; width: 1200px; height: 799px; }

  .card {
    position: absolute; top: 251px;
    width: 520px; height: 297px;
    background: var(--white);
    box-shadow: 0 6px 18px rgba(0,0,0,.18);
    overflow: hidden;
  }
  .card--front { left: 60px; }
  .card--back { left: 620px; }

  /* Front */
  .front-band {
    position: absolute; left: 0; right: 0; top: 58px; bottom: 0;
    background: var(--band);
  }
  .brand {
    position: absolute; left: 0; right: 0; top: 0; bottom: 0;
    display: flex; align-items: center; justify-content: center; gap: 14px;
  }
  .brand-dot {
    width: 46px; height: 46px; border-radius: 50%;
    background: var(--green);
  }
  .brand-name {
    font-weight: 900; font-size: 46px; color: var(--light);
    letter-spacing: .5px;
  }

  /* Back */
  .back-band {
    position: absolute; left: 0; right: 0; top: 70px; height: 178px;
    background: var(--band);
  }
  .holder {
    position: absolute; left: 18px; top: 22px;
    display: flex; align-items: center; gap: 10px;
  }
  .holder-icon {
    width: 32px; height: 32px; border-radius: 50%;
    background: var(--green);
    display: flex; align-items: center; justify-content: center;
  }
  .holder-name { font-size: 16px; font-weight: 700; color: var(--ink); line-height: 1; letter-spacing: .3px; }
  .holder-role { font-size: 12px; font-weight: 400; color: var(--ink-soft); margin-top: 2px; }

  .contacts {
    position: absolute; left: 28px; top: 92px;
    list-style: none;
  }
  .contact {
    display: flex; align-items: center; gap: 10px;
    height: 24px; margin-bottom: 18px;
    color: var(--light); font-size: 13px; font-weight: 400;
  }
  .contact-icon {
    width: 24px; height: 24px; border-radius: 3px;
    background: var(--green);
    display: flex; align-items: center; justify-content: center;
  }

  .tag {
    position: absolute; left: 300px; top: 44px;
    width: 176px; height: 136px;
  }
  .tag-curl {
    position: absolute; left: 0; top: 0; width: 176px; height: 34px;
    background: var(--green-dark);
    border-radius: 14px 14px 0 0;
  }
  .tag-body {
    position: absolute; left: 0; top: 16px; width: 176px; height: 120px;
    background: var(--green);
    border-radius: 14px 0 14px 14px;
    box-shadow: 0 4px 8px rgba(0,0,0,.25);
    display: flex; flex-direction: column; justify-content: center; align-items: center;
    color: var(--light); text-align: center;
  }
  .tag-lead { font-size: 11px; font-weight: 300; letter-spacing: .4px; }
  .tag-title { font-size: 18px; font-weight: 700; letter-spacing: .6px; margin-top: 2px; }
</style>
</head>
<body>
<main class="stage">

  <section class="card card--front" aria-label="Card front">
    <div class="front-band"></div>
    <div class="brand">
      <span class="brand-dot"></span>
      <span class="brand-name">Nit Clear</span>
    </div>
  </section>

  <section class="card card--back" aria-label="Card back">
    <div class="back-band"></div>

    <div class="holder">
      <div class="holder-icon">
        <svg width="18" height="18" viewBox="0 0 18 18" aria-hidden="true">
          <circle cx="9" cy="6" r="3.6" fill="#fff"/>
          <path d="M2.5 16c0-3.6 2.9-5.6 6.5-5.6s6.5 2 6.5 5.6z" fill="#fff"/>
        </svg>
      </div>
      <div>
        <p class="holder-name">DANA WHITFIELD</p>
        <p class="holder-role">Owner</p>
      </div>
    </div>

    <ul class="contacts">
      <li class="contact">
        <span class="contact-icon">
          <svg width="14" height="14" viewBox="0 0 14 14" aria-hidden="true">
            <path d="M3 1.5l2 .2 1 3-1.4 1a7 7 0 0 0 3.7 3.7l1-1.4 3 1 .2 2c0 .8-.7 1.5-1.5 1.5A10.5 10.5 0 0 1 1.5 3C1.5 2.2 2.2 1.5 3 1.5z" fill="#fff"/>
          </svg>
        </span>
        1-800-555-NITS (6487)
      </li>
      <li class="contact">
        <span class="contact-icon">
          <svg width="14" height="14" viewBox="0 0 14 14" aria-hidden="true" fill="none" stroke="#fff" stroke-width="1.3">
            <circle cx="7" cy="7" r="5.5"/>
            <ellipse cx="7" cy="7" rx="2.4" ry="5.5"/>
            <path d="M1.5 7h11"/>
          </svg>
        </span>
        www.nitclear.com
      </li>
      <li class="contact">
        <span class="contact-icon">
          <svg width="14" height="14" viewBox="0 0 14 14" aria-hidden="true">
            <rect x="1.5" y="3" width="11" height="8" rx="1" fill="#fff"/>
            <path d="M1.8 3.4L7 7.6l5.2-4.2" fill="none" stroke="#7cc242" stroke-width="1.2"/>
          </svg>
        </span>
        dana@nitclear.com
      </li>
    </ul>

    <div class="tag">
      <div class="tag-curl"></div>
      <div class="tag-body">
        <p class="tag-lead">ALL NATURAL IN-HOME</p>
        <p class="tag-title">LICE REMOVAL</p>
      </div>
    </div>
  </section>

</main>
</body>
</html>
```